Save the Date postcard for Oak Hollow School 18th Annual Gala Evening - Marivela: Where the Fiesta

We need a Save the Date postcard for our school's Gala Evening fundraiser. Front of postcard should be tropical to invoke the feel of Copacabana, with bright colors, flowers, palm leaves, and fruit. We would like the design to include a logo that could be used for future projects like letterhead and invitation with the selected designer. I will attach a file with a design similar to what I would like to see as well as files from past years for our event.

Info that must be included:
Oak Hollow 18th Annual Gala Evening
Copacabana
Where the Fiesta Keeps Glowing!
March 10, 2018 5:30-Midnight
Brindle Court Hotel - Ridgeway Hall
The back side should leave the right side blank with mailing address space. On the left side, one small graphic like flower or palm leaf on front with the following info:
(Return address) Oak Hollow Parish School
486 North Lorrin
Larkfield, TX 75412
(Tagline) Bring your yellow feathers and dancing shoes because music and passion are ALWAYS in fashion...
Save the date for a seat at the hottest spot north of Havana on March 10!
(Footer) Sponsor & Ticket Information soon!
oakhollow-prep.org/ohs-gala-evening/
Oak Hollow is a 501(c)(3) organization

Target Market(s)

Affluent supporters and donors, age 21+

Industry/Entity Type

School

Font styles to use
Serif
Decorative

Colors

Designer to choose colors to be used in the design.

Requirements
Must have
• Text as specified in description
Nice to have
• Bright colors, palm leaves, and fruit
Should not have
• Don't use typical lady with fruit on head or anything risque

```html
<!DOCTYPE html>
<html lang="en">
<head>
<meta charset="utf-8">
<title>Oak Hollow 18th Annual Gala Evening – Save the Date Postcard</title>
<link rel="stylesheet" href="https://fonts.googleapis.com/css2?family=Alfa+Slab+One&family=Bree+Serif&family=Kaushan+Script&family=Montserrat:wght@600;700&family=Oswald:wght@600&family=Roboto+Condensed:wght@400;700&display=swap">
<style>
  :root {
    --backdrop: #ece7df;
    --front-orange: #f2471d;
    --front-border: #ff5a26;
    --gold-light: #f7d774;
    --gold-dark: #c8961f;
    --cream: #fff3b8;
    --white: #ffffff;
    --ink: #1e1a1a;
    --script-pink: #e4399b;
    --script-violet: #c23ad8;
    --blush: #f6b3b0;
    --violet: #a25ab6;
    --url-violet: #a76bc1;
    --parish-blue: #1f4fa3;
    --stamp-grey: #b9bdc1;
    --tropic-green: #3f9b6a;
    --tropic-pink: #ef5c8f;
  }
  * { box-sizing: border-box; margin: 0; padding: 0; }
  html, body { width: 1200px; height: 480px; overflow: hidden; }
  body { background: var(--backdrop); position: relative; font-family: "Montserrat", sans-serif; }

  /* ---------- Front ---------- */
  .card-front {
    position: absolute; left: 42px; top: 32px; width: 548px; height: 414px;
    background: var(--front-border);
  }
  .gold-frame {
    position: absolute; left: 13px; top: 13px; right: 13px; bottom: 13px;
    background: linear-gradient(135deg, var(--gold-light), var(--gold-dark) 30%, var(--gold-light) 55%, var(--gold-dark) 80%, var(--gold-light));
  }
  .front-field {
    position: absolute; left: 12px; top: 12px; right: 12px; bottom: 12px;
    background: var(--front-orange);
  }
  .event-heading {
    position: absolute; top: 16px; width: 100%; text-align: center;
    font-family: "Bree Serif", serif; font-style: italic; font-weight: 400; font-size: 24px;
    color: var(--cream); letter-spacing: 0.3px;
  }
  .tropical-art {
    position: absolute; left: 110px; top: 58px; width: 300px; height: 258px;
    border-radius: 48% 52% 45% 55%;
    background: radial-gradient(circle at 55% 55%, var(--tropic-pink) 0%, #d9487a 28%, var(--tropic-green) 55%, rgba(63,155,106,0) 74%);
  }
  .title-art { position: absolute; left: 0; top: 92px; width: 100%; height: 110px; }
  .title-word {
    font-family: "Alfa Slab One", serif; font-size: 62px; fill: var(--white);
    stroke: #c9b8a2; stroke-width: 1; paint-order: stroke;
    filter: drop-shadow(4px 5px 0 #b7341a);
  }
  .tagline-script {
    position: absolute; top: 204px; width: 100%; text-align: center;
    font-family: "Kaushan Script", cursive; font-size: 30px; line-height: 34px;
    color: var(--script-violet);
    text-shadow: 2px 2px 0 var(--white), -1px -1px 0 var(--white), 1px -1px 0 var(--white), -1px 1px 0 var(--white);
  }
  .event-date {
    position: absolute; top: 290px; width: 100%; text-align: center;
    font-weight: 600; font-size: 19px; color: var(--white);
  }
  .event-venue {
    position: absolute; top: 318px; width: 100%; text-align: center;
    font-weight: 700; font-size: 14px; line-height: 18px; color: var(--ink);
  }

  /* ---------- Back ---------- */
  .card-back {
    position: absolute; left: 620px; top: 32px; width: 537px; height: 414px;
    background: linear-gradient(90deg, var(--blush) 0%, #fbdcda 38%, var(--white) 62%);
    box-shadow: 0 0 0 1px rgba(0,0,0,0.04);
  }
  .back-tagline {
    position: absolute; left: 15px; top: 40px; width: 250px; text-align: center;
    font-family: "Kaushan Script", cursive; font-size: 12.5px; line-height: 20px; color: var(--ink);
  }
  .back-tagline em { font-style: normal; color: var(--script-pink); }
  .floral-wreath {
    position: absolute; left: 18px; top: 112px; width: 200px; height: 200px; border-radius: 50%;
    background: radial-gradient(circle, rgba(239,92,143,0.55) 45%, rgba(63,155,106,0.45) 62%, rgba(63,155,106,0) 72%);
  }
  .save-badge {
    position: absolute; left: 50px; top: 145px; width: 132px; height: 132px; border-radius: 50%;
    background: var(--violet); color: var(--white); text-align: center;
    font-family: "Roboto Condensed", sans-serif; border: 2px solid rgba(255,255,255,0.6);
    padding-top: 26px;
  }
  .save-badge .save-headline { font-family: "Oswald", sans-serif; font-weight: 600; font-size: 18px; line-height: 20px; }
  .save-badge .save-detail { font-weight: 700; font-size: 11.5px; line-height: 14px; margin-top: 2px; }
  .save-badge .save-when { font-family: "Oswald", sans-serif; font-weight: 600; font-size: 14px; margin-top: 3px; }
  .sponsor-note {
    position: absolute; left: 20px; top: 313px; width: 230px; text-align: center;
    font-family: "Oswald", sans-serif; font-weight: 600; font-size: 13px; color: var(--ink);
  }
  .event-url {
    position: absolute; left: 28px; top: 338px; width: 214px; height: 22px;
    background: var(--url-violet); color: var(--white); text-align: center;
    font-family: "Roboto Condensed", sans-serif; font-weight: 700; font-size: 12px; line-height: 22px;
  }
  .nonprofit-note {
    position: absolute; left: 20px; top: 362px; width: 230px; text-align: center;
    font-family: "Roboto Condensed", sans-serif; font-size: 10.5px; color: var(--ink);
  }
  .school-mark {
    position: absolute; left: 303px; top: 24px; width: 110px; text-align: center;
    font-family: "Roboto Condensed", sans-serif; font-weight: 700; font-size: 11px; line-height: 13px;
    color: var(--parish-blue);
  }
  .school-mark .mark-square {
    display: block; width: 34px; height: 34px; margin: 0 auto 6px; background: var(--parish-blue);
  }
  .return-address {
    position: absolute; left: 310px; top: 93px; font-style: normal;
    font-family: "Roboto Condensed", sans-serif; font-size: 11px; line-height: 15px; color: var(--ink);
  }
  .stamp-box {
    position: absolute; left: 420px; top: 13px; width: 75px; height: 76px;
    border: 3px solid var(--stamp-grey); background: var(--white);
  }
</style>
</head>
<body>
  <section class="card-front" aria-label="Postcard front">
    <div class="gold-frame">
      <div class="front-field">
        <h1 class="event-heading">Oak Hollow 18th Annual Gala Evening</h1>
        <div class="tropical-art" role="img" aria-label="Tropical arrangement of hibiscus flowers, palm leaves, pineapple and a toucan"></div>
        <svg class="title-art" viewBox="0 0 500 110" aria-label="Marivela">
          <defs><path id="title-arc" d="M40 100 Q250 30 460 100"/></defs>
          <text class="title-word" text-anchor="middle"><textPath href="#title-arc" startOffset="50%">MARIVELA</textPath></text>
        </svg>
        <p class="tagline-script">Where the Fiesta<br>Keeps Glowing!</p>
        <p class="event-date">March 10, 2018 5:30-Midnight</p>
        <p class="event-venue">Brindle Court Hotel<br>Ridgeway Hall</p>
      </div>
    </div>
  </section>

  <section class="card-back" aria-label="Postcard back">
    <p class="back-tagline">Bring your yellow feathers<br>and dancing shoes because<br>music and passion<br>are <em>Always</em> in fashion...</p>
    <div class="floral-wreath" role="img" aria-label="Wreath of tropical flowers and leaves"></div>
    <div class="save-badge">
      <p class="save-headline">SAVE THE DATE</p>
      <p class="save-detail">for a seat at the hottest<br>spot north of Havana</p>
      <p class="save-when">on March 10!</p>
    </div>
    <p class="sponsor-note">SPONSOR &amp; TICKET INFORMATION SOON!</p>
    <p class="event-url">oakhollow-prep.org/ohs-gala-evening/</p>
    <p class="nonprofit-note">Oak Hollow is a 501(c)(3) organization</p>

    <div class="school-mark"><span class="mark-square"></span>Oak Hollow</div>
    <address class="return-address">Oak Hollow Parish School<br>486 North Lorrin<br>Larkfield, TX 75412</address>
    <div class="stamp-box" aria-label="Stamp area"></div>
  </section>
</body>
</html>
```